Brantley Advisory Group provides support for renewable energy projects to utilities and suppliers

I need a professional looking business card that is both simple and elegant and unique. My clients are mostly large organizations not individuals. I am a consultant with my own company that is small but would like to give clients the impression I am larger. Smart grid, fiber optics, software, field hardware, distribution automation, substation automation, operations, energy storage/batteries, microgrids, customer service, strategy/roadmaps, conservation, Automated Metering Infrastruture (AMI or smart meters) are all areas of focus.

Target Market(s)

Utilities, suppliers, governmental agencies involved in energy. All types of energy especially natural gas and electrical. Especially renewable energy or green projects.

Contact Information for Business Card

Name - Mark Brantley Cell Phone - 425.318.2746 Email - mbrantley@brantleyag-example.com
Company - Brantley Advisory Group (logo) Title - Principal

Font styles to use
Serif
Sans Serif

Colors

Designer to choose colors to be used in the design.

Requirements
Must have
• Simple and professional and powerful.
• Unique/creative design.
Nice to have
• Utilize color scheme to accent logo colors. Maybe some geometric pattern on edge of card with color.
Should not have
• Busy, complicated, traditional

```html
<!DOCTYPE html>
<html lang="en">
<head>
<meta charset="utf-8">
<title>Brantley Advisory Group – Business Card</title>
<link href="https://fonts.googleapis.com/css2?family=Lato:wght@400;700&display=swap" rel="stylesheet">
<style>
  :root {
    --bg: #8a8a8a;
    --card-white: #ffffff;
    --brand-blue: #1b3f96;
    --brand-green: #6a9a3e;
    --text-grey: #858585;
    --white: #ffffff;
  }
  * { margin: 0; padding: 0; box-sizing: border-box; }
  html, body {
    width: 1200px;
    height: 960px;
    overflow: hidden;
    background: var(--bg);
    font-family: "Lato", Arial, sans-serif;
  }
  .canvas {
    position: relative;
    width: 1200px;
    height: 960px;
  }
  .card {
    position: absolute;
    left: 272px;
    width: 656px;
    height: 374px;
    border-radius: 24px;
    overflow: hidden;
  }
  .card--front { top: 59px; background: var(--card-white); }
  .card--back  { top: 506px; background: var(--brand-blue); }

  /* Front */
  .wordmark {
    position: absolute;
    left: 58px;
    top: 76px;
    display: flex;
    align-items: center;
    gap: 12px;
    font-weight: 700;
    font-size: 25px;
    color: var(--brand-blue);
    letter-spacing: 0.2px;
  }
  .wordmark__square {
    width: 22px;
    height: 22px;
    background: var(--brand-green);
    border-radius: 3px;
  }
  .person {
    position: absolute;
    left: 67px;
    top: 243px;
  }
  .person__name {
    font-weight: 700;
    font-size: 27px;
    color: var(--brand-blue);
    line-height: 1.1;
  }
  .person__title {
    font-size: 19px;
    color: var(--text-grey);
    margin-top: 6px;
  }
  .contact {
    position: absolute;
    left: 345px;
    top: 249px;
    list-style: none;
  }
  .contact__item {
    display: flex;
    align-items: center;
    gap: 9px;
    font-size: 17.5px;
    color: var(--text-grey);
    line-height: 24px;
  }
  .contact__icon { width: 14px; height: 14px; flex: none; }

  /* Back */
  .back-wordmark {
    position: absolute;
    left: 0;
    right: 0;
    top: 145px;
    display: flex;
    justify-content: center;
    align-items: center;
    gap: 14px;
    font-weight: 700;
    font-size: 36px;
    color: var(--white);
  }
  .back-wordmark__square {
    width: 30px;
    height: 30px;
    background: var(--brand-green);
    border-radius: 4px;
  }
  .back-url {
    position: absolute;
    left: 0;
    right: 0;
    top: 304px;
    text-align: center;
    font-size: 17px;
    letter-spacing: 1.5px;
    color: var(--white);
  }
</style>
</head>
<body>
<main class="canvas">
  <section class="card card--front">
    <div class="wordmark"><span class="wordmark__square"></span>Brantley Advisory Group</div>

    <div class="person">
      <p class="person__name">Mark Brantley</p>
      <p class="person__title">Principal</p>
    </div>

    <ul class="contact">
      <li class="contact__item">
        <svg class="contact__icon" viewBox="0 0 16 16" aria-hidden="true"><path d="M4 1.5c.6 0 1.1.4 1.3 1l.8 2.3c.2.5 0 1-.4 1.3l-1 .8c.8 1.7 2 2.9 3.6 3.7l.9-1c.3-.4.9-.5 1.3-.3l2.3.9c.5.2.8.8.7 1.3l-.4 2c-.1.6-.7 1-1.3.9C6.4 13.9 2.2 9.6 1.6 4c0-.6.4-1.2 1-1.3z" fill="var(--brand-blue)"/></svg>
        425.318.2746
      </li>
      <li class="contact__item">
        <svg class="contact__icon" viewBox="0 0 16 16" aria-hidden="true"><rect x="1" y="3.5" width="14" height="9" fill="var(--brand-blue)"/><path d="M1.5 4l6.5 5 6.5-5" stroke="#fff" stroke-width="1.2" fill="none"/></svg>
        mbrantley@brantleyag-example.com
      </li>
      <li class="contact__item">
        <svg class="contact__icon" viewBox="0 0 16 16" aria-hidden="true"><g fill="none" stroke="var(--brand-blue)" stroke-width="1.2"><circle cx="8" cy="8" r="6.5"/><ellipse cx="8" cy="8" rx="3" ry="6.5"/><path d="M1.5 8h13M2.5 4.8h11M2.5 11.2h11"/></g></svg>
        www.brantleyag-example.com
      </li>
    </ul>
  </section>

  <section class="card card--back">
    <div class="back-wordmark"><span class="back-wordmark__square"></span>Brantley Advisory Group</div>
    <p class="back-url">www.brantleyag-example.com</p>
  </section>
</main>
</body>
</html>
```